business card Quintavo

Wee need a business card design for a new compagny based on Paris
We developped innovative a platform for selling services to refresh, beautify and develop its housing.
We would like a red logo on a black background
Te final design should communicate quality service, know-how, high-end

Target Market(s)

individuals

Industry/Entity Type

Business

```html
<!DOCTYPE html>
<html lang="en">
<head>
<meta charset="utf-8">
<title>Quintavo business card</title>
<link rel="stylesheet" href="https://fonts.googleapis.com/css2?family=Questrial&display=swap">
<style>
  :root {
    --stage: #3b3b3d;
    --card-red: #ff5a61;
    --card-red-deep: #f54850;
    --card-grey: #8f8f91;
    --divider: #d9d9d9;
    --text-light: #ffffff;
    --text-soft: #f1f1f1;
    --brand-grey: #7c7c7e;
  }
  * { box-sizing: border-box; margin: 0; padding: 0; }
  html, body {
    width: 1200px; height: 780px; overflow: hidden;
    background: var(--stage);
    font-family: "Questrial", "Century Gothic", sans-serif;
  }
  .stage {
    width: 1200px; height: 780px;
    display: flex; align-items: center; justify-content: center; gap: 60px;
  }
  .card {
    width: 510px; height: 292px;
    border-radius: 22px;
    overflow: hidden;
    position: relative;
    background: var(--card-red);
    box-shadow: 0 14px 30px rgba(0,0,0,.35);
  }
  /* Front */
  .card-front .info-panel {
    position: absolute; left: 0; top: 0; right: 0; height: 176px;
    background: var(--card-grey);
    border-bottom: 5px solid var(--divider);
    padding: 28px 34px 0;
    color: var(--text-light);
    display: flex; justify-content: space-between;
  }
  .person-name { font-size: 25px; letter-spacing: 1.5px; text-transform: uppercase; }
  .person-role { font-size: 12px; font-style: italic; color: var(--text-soft); margin-top: 4px; }
  .address { font-size: 12.5px; line-height: 1.35; margin-top: 18px; color: var(--text-soft); }
  .contact-list { list-style: none; margin-top: 40px; font-size: 12px; color: var(--text-soft); }
  .contact-list li { display: flex; align-items: center; gap: 14px; height: 22px; }
  .contact-icon { width: 15px; height: 15px; flex: none; }
  .card-front .brand-band {
    position: absolute; left: 0; right: 0; bottom: 0; height: 116px;
    display: flex; align-items: center; justify-content: flex-end;
    padding-right: 34px;
  }
  .brand { display: flex; align-items: center; gap: 14px; }
  .brand-mark { width: 20px; height: 20px; border: 2.5px solid var(--text-light); border-radius: 3px; }
  .brand-name { font-size: 36px; color: var(--brand-grey); letter-spacing: 1px; }
  /* Back */
  .card-back {
    display: flex; align-items: center; justify-content: center;
  }
  .card-back .brand-mark { width: 28px; height: 28px; border-width: 3px; }
  .card-back .brand-name { font-size: 48px; }
</style>
</head>
<body>
<main class="stage">
  <section class="card card-front" aria-label="Business card front">
    <div class="info-panel">
      <div class="identity">
        <h1 class="person-name">Marc Delorme</h1>
        <p class="person-role">Inspector QRS 7-204</p>
        <p class="address">2140 Alder Lane West<br>Springfield, ST 00412</p>
      </div>
      <ul class="contact-list">
        <li>
          <svg class="contact-icon" viewBox="0 0 16 16" aria-hidden="true"><circle cx="8" cy="8" r="7.5" fill="#b5b5b7"/><path d="M5.4 4.3l1.3-.3.8 2-1 .7c.5 1.1 1.3 1.9 2.4 2.4l.7-1 2 .8-.3 1.3c-3.4.1-6-2.5-5.9-5.9z" fill="#fff"/></svg>
          555 014 2290
        </li>
        <li>
          <svg class="contact-icon" viewBox="0 0 16 16" aria-hidden="true"><circle cx="8" cy="8" r="7.5" fill="#b5b5b7"/><rect x="4.2" y="5" width="7.6" height="6" rx="1" fill="none" stroke="#fff" stroke-width="1.1"/><line x1="4.2" y1="7" x2="11.8" y2="7" stroke="#fff" stroke-width="1"/></svg>
          www.Quintavo.com
        </li>
        <li>
          <svg class="contact-icon" viewBox="0 0 16 16" aria-hidden="true"><circle cx="8" cy="8" r="7.5" fill="#b5b5b7"/><rect x="4" y="5.3" width="8" height="5.4" rx=".6" fill="none" stroke="#fff" stroke-width="1.1"/><path d="M4.2 5.6L8 8.4l3.8-2.8" fill="none" stroke="#fff" stroke-width="1"/></svg>
          Marc@Quintavo.com
        </li>
      </ul>
    </div>
    <div class="brand-band">
      <div class="brand">
        <span class="brand-mark" aria-hidden="true"></span>
        <span class="brand-name">Quintavo</span>
      </div>
    </div>
  </section>

  <section class="card card-back" aria-label="Business card back">
    <div class="brand">
      <span class="brand-mark" aria-hidden="true"></span>
      <span class="brand-name">Quintavo</span>
    </div>
  </section>
</main>
</body>
</html>
```